Business cards for education company

We need a business card design for a relatively new company based in Queensland and operating across Australia. We resell diploma level education courses which include Business, Management, Finance, Community Services & Government courses. We offer over 20 different courses.
The target market is for anyone 16 years of age and older. There is no age limit.

We would like to see the design use the color blue and silver. The final design should communicate professionalism and a bright future.

We sell education but are also promoting the career they see themselves in 2-3 years in the future

Our company logo is attached.

Target Market(s)

We target all age groups above 16 years of age. The main target market would be people aged between 17-35.

We focus on those people who cannot make it into University or do not want to commit the time to a full degree.

Industry/Entity Type

Education

Requirements
Must have
• Professional
Company logo
website
Contact details:

Please use the following example:

Lionel Parfitt
Senior Education Consultant
0417 386 591
Lionel.parfitt@brightwaylearninghub.com.au
www.brightwaylearninghub.com.au

```html
<!DOCTYPE html>
<html lang="en">
<head>
<meta charset="utf-8">
<title>Brightway Learning Hub – Business Card</title>
<link rel="stylesheet" href="https://fonts.googleapis.com/css2?family=Roboto+Condensed:wght@400;700&display=swap">
<style>
  :root {
    --page-bg: #e9e9e9;
    --card-black: #1a1a1a;
    --card-black-deep: #0e0e0e;
    --silver-light: #ffffff;
    --silver-mid: #e4e6e8;
    --silver-dark: #c9ccd0;
    --brand-blue: #1e8fd0;
    --icon-blue: #3a9fe0;
    --text-light: #f2f2f2;
    --text-muted: #d6d6d6;
  }
  * { box-sizing: border-box; margin: 0; padding: 0; }
  html, body {
    width: 1200px;
    height: 1023px;
    overflow: hidden;
    background: var(--page-bg);
    font-family: "Roboto Condensed", "Arial Narrow", sans-serif;
  }
  .stage {
    width: 1200px;
    height: 1023px;
    display: flex;
    flex-direction: column;
    align-items: center;
    justify-content: center;
    gap: 36px;
  }
  .card {
    position: relative;
    width: 820px;
    height: 468px;
    box-shadow: 0 10px 26px rgba(0,0,0,0.22);
    overflow: hidden;
  }

  /* Front */
  .card--front {
    background: linear-gradient(160deg, #222 0%, var(--card-black) 45%, var(--card-black-deep) 100%);
  }
  .card__top-strip {
    position: absolute;
    left: 0; top: 0;
    width: 100%;
    height: 55px;
    background: var(--card-black);
  }
  .card__brand-band {
    position: absolute;
    left: 0; top: 55px;
    width: 100%;
    height: 140px;
    background: linear-gradient(180deg, var(--silver-light) 0%, var(--silver-mid) 70%, var(--silver-dark) 100%);
    display: flex;
    align-items: center;
    padding-left: 47px;
    gap: 20px;
  }
  .brand__mark {
    width: 75px;
    height: 75px;
    flex: none;
    background: var(--brand-blue);
  }
  .brand__name {
    color: var(--brand-blue);
    font-weight: 700;
    font-size: 46px;
    letter-spacing: 1px;
    text-transform: uppercase;
    line-height: 1;
    white-space: nowrap;
  }
  .contact-list {
    position: absolute;
    left: 47px;
    top: 236px;
    list-style: none;
    display: flex;
    flex-direction: column;
    gap: 26px;
  }
  .contact-list__item {
    display: flex;
    align-items: center;
    gap: 19px;
    color: var(--text-light);
    font-size: 20px;
    white-space: nowrap;
  }
  .contact-list__icon {
    width: 27px;
    height: 27px;
    flex: none;
  }
  .person {
    position: absolute;
    right: 55px;
    top: 234px;
  }
  .person__name {
    color: var(--brand-blue);
    font-weight: 700;
    font-size: 31px;
    line-height: 1.1;
  }
  .person__title {
    color: var(--text-muted);
    font-size: 20px;
    margin-top: 8px;
  }

  /* Back */
  .card--back {
    background: linear-gradient(170deg, var(--silver-light) 0%, var(--silver-mid) 65%, var(--silver-dark) 100%);
    display: flex;
    align-items: center;
    justify-content: center;
    gap: 24px;
  }
  .card--back .brand__mark {
    width: 90px;
    height: 90px;
  }
  .card--back .brand__name {
    font-size: 52px;
  }
</style>
</head>
<body>
<main class="stage">
  <article class="card card--front">
    <div class="card__top-strip"></div>

    <header class="card__brand-band">
      <div class="brand__mark"></div>
      <div class="brand__name">Brightway Learning Hub</div>
    </header>

    <ul class="contact-list">
      <li class="contact-list__item">
        <svg class="contact-list__icon" viewBox="0 0 34 34" aria-hidden="true">
          <rect width="34" height="34" rx="4" fill="var(--icon-blue)"/>
          <path d="M11 8c1.5 0 3 3 3 4.5S12 14 12.5 15.5s4 5.5 5.5 6 2-1.5 3.5-1.5 4.5 1.5 4.5 3-2 3-4 3C14 26 8 20 8 12c0-2 1.5-4 3-4z" fill="#fff"/>
        </svg>
        <span>0417 386 591</span>
      </li>
      <li class="contact-list__item">
        <svg class="contact-list__icon" viewBox="0 0 34 34" aria-hidden="true">
          <rect width="34" height="34" rx="4" fill="var(--icon-blue)"/>
          <rect x="7" y="10" width="20" height="14" fill="#fff"/>
          <path d="M7 10l10 8 10-8" fill="none" stroke="var(--icon-blue)" stroke-width="2"/>
        </svg>
        <span>Lionel.parfitt@brightwaylearninghub.com.au</span>
      </li>
      <li class="contact-list__item">
        <svg class="contact-list__icon" viewBox="0 0 34 34" aria-hidden="true">
          <rect width="34" height="34" rx="4" fill="var(--icon-blue)"/>
          <circle cx="17" cy="17" r="9" fill="none" stroke="#fff" stroke-width="2"/>
          <ellipse cx="17" cy="17" rx="4" ry="9" fill="none" stroke="#fff" stroke-width="1.6"/>
          <line x1="8" y1="17" x2="26" y2="17" stroke="#fff" stroke-width="1.6"/>
        </svg>
        <span>www.brightwaylearninghub.com.au</span>
      </li>
    </ul>

    <section class="person">
      <h1 class="person__name">Lionel Parfitt</h1>
      <p class="person__title">Senior Education Consultant</p>
    </section>
  </article>

  <article class="card card--back">
    <div class="brand__mark"></div>
    <div class="brand__name">Brightway Learning Hub</div>
  </article>
</main>
</body>
</html>
```